Auto glass company

BRIGHTWAY
Roving Auto Glass, LLC
555-604-1937

* Windshield Replacement
* Rock Chip Repair
Danny "K"
Brightwayrovingautoglass@example.com
* Fully Insured

This is what I would like on the card. The image is what I had before. Looking for a logo possible too, couldn’t find a place to add that on. It’s a auto glass company.

Target Market(s)

Auto glass

Industry/Entity Type

Auto glass

Contact Information for Business Card

Logo, business name, phone number, windshield replacement, rock chip repair, insured, owner name Danny K, email address brightwayrovingautoglass@example.com

Colors

Designer to choose colors to be used in the design.

Requirements
Must have
• Logo, business name, phone number, windshield replacement, rock chip repair, insured, owner name Danny K, email address brightwayrovingautoglass@example.com

```html
<!DOCTYPE html>
<html lang="en">
<head>
<meta charset="utf-8">
<title>Brightway Roving Auto Glass – Business Card</title>
<link href="https://fonts.googleapis.com/css2?family=Jost:wght@300;400;500&display=swap" rel="stylesheet">
<style>
  :root {
    --navy: #15203d;
    --orange: #e2761c;
    --cream: #e9e0cf;
    --ink: #2c2d33;
    --card: #eef0f1;
    --stage: #d8d3cb;
  }
  html, body {
    margin: 0;
    width: 1200px;
    height: 969px;
    overflow: hidden;
    background: var(--stage);
    font-family: "Jost", "Futura", sans-serif;
  }
  .card {
    position: absolute;
    left: 57px;
    top: 175px;
    width: 1085px;
    height: 618px;
    background: var(--card);
    box-shadow: 0 0 0 1px #c9cbcf, 0 18px 40px rgba(0,0,0,.18);
    overflow: hidden;
  }
  .brand-block {
    position: absolute;
    left: 0;
    top: 116px;
    width: 91px;
    height: 97px;
    background: var(--navy);
  }
  .brand {
    position: absolute;
    left: 110px;
    top: 116px;
    width: 480px;
    height: 97px;
    margin: 0;
    display: flex;
    flex-direction: column;
    justify-content: center;
    color: var(--navy);
    font-weight: 500;
    white-space: nowrap;
  }
  .brand-name {
    font-size: 56px;
    line-height: 1;
  }
  .brand-tagline {
    font-size: 22px;
    line-height: 1.3;
    margin-top: 4px;
  }
  .owner-band {
    position: absolute;
    left: 609px;
    top: 116px;
    width: 476px;
    height: 97px;
    background: var(--navy);
    display: flex;
    align-items: center;
    justify-content: flex-end;
    padding-right: 57px;
    box-sizing: border-box;
    white-space: nowrap;
  }
  .owner-name { font-size: 46px; font-weight: 500; color: var(--cream); }
  .owner-slash { font-size: 50px; font-weight: 300; color: var(--cream); margin: 0 10px 0 14px; }
  .owner-role { font-size: 34px; font-weight: 300; color: var(--orange); margin-top: 8px; }

  .contact {
    position: absolute;
    left: 105px;
    top: 440px;
    color: var(--ink);
  }
  .contact-line { display: flex; align-items: center; white-space: nowrap; }
  .contact-line svg { width: 28px; flex: none; margin-right: 14px; }
  .phone { font-size: 44px; font-weight: 300; height: 58px; }
  .email { font-size: 24px; font-weight: 400; height: 34px; }

  .accent-rule {
    position: absolute;
    left: 105px;
    top: 606px;
    width: 470px;
    height: 12px;
    background: var(--orange);
  }
  .services {
    position: absolute;
    right: 58px;
    top: 428px;
    margin: 0;
    padding: 0;
    list-style: none;
    text-align: right;
    color: var(--navy);
    font-size: 26px;
    font-weight: 400;
    letter-spacing: -0.4px;
  }
  .services li { display: flex; align-items: center; justify-content: flex-end; height: 31px; }
  .services svg { width: 22px; height: 22px; margin-left: 10px; }
  .side-bar {
    position: absolute;
    left: 1072px;
    top: 433px;
    width: 11px;
    height: 83px;
    background: var(--navy);
  }
</style>
</head>
<body>
  <div class="card">
    <div class="brand-block"></div>
    <h1 class="brand">
      <span class="brand-name">BRIGHTWAY</span>
      <span class="brand-tagline">Roving Auto Glass, LLC</span>
    </h1>

    <div class="owner-band">
      <span class="owner-name">DANNY K</span><span class="owner-slash">/</span><span class="owner-role">OWNER</span>
    </div>

    <div class="contact">
      <div class="contact-line phone">
        <svg viewBox="0 0 24 24" fill="var(--orange)"><path d="M6.6 2.5c.6-.4 1.4-.2 1.8.4l2 3.2c.4.6.2 1.3-.3 1.7L8.6 8.9c.9 2.4 3 4.6 5.4 5.6l1.3-1.5c.4-.5 1.2-.7 1.7-.3l3.2 2c.6.4.8 1.2.4 1.8l-1.2 2c-.6 1-1.8 1.5-3 1.2C9.8 18.3 5.2 13.6 3.8 7.1c-.3-1.2.2-2.4 1.2-3z"/></svg>
        555-604-1937
      </div>
      <div class="contact-line email">
        <svg viewBox="0 0 24 16" fill="none" stroke="var(--orange)" stroke-width="2.2"><rect x="1.5" y="1.5" width="21" height="13" fill="var(--orange)" stroke="none"/><path d="M2 2l10 7 10-7" stroke="var(--card)"/></svg>
        brightwayrovingautoglass@example.com
      </div>
    </div>

    <div class="accent-rule"></div>

    <ul class="services">
      <li>WINDSHIELD REPLACEMENT<svg viewBox="0 0 22 22" fill="none" stroke="var(--orange)" stroke-width="2.4"><rect x="2" y="4" width="16" height="16"/><path d="M6 11l4 4 10-12"/></svg></li>
      <li>ROCK CHIP REPAIR<svg viewBox="0 0 22 22" fill="none" stroke="var(--orange)" stroke-width="2.4"><rect x="2" y="4" width="16" height="16"/><path d="M6 11l4 4 10-12"/></svg></li>
      <li>FULLY INSURED<svg viewBox="0 0 22 22" fill="none" stroke="var(--orange)" stroke-width="2.4"><rect x="2" y="4" width="16" height="16"/><path d="M6 11l4 4 10-12"/></svg></li>
    </ul>
    <div class="side-bar"></div>
  </div>
</body>
</html>
```